Pelton|Marsh & Quillan business card contest

We need a logo for an upscale boutique diversified company involved in real estate, investments, cattle, and more. Our businesses DO NOT need to be reflected in the business card nor do we want them noted. This is our logo and colors and we love our logo and colors. Our logo looks best against a black background and we like to include the firm name in our logo usage. importantly, the names Pelton and Marsh are separated by | not / and we use an ampersand not the word and.
On the front of the card, we want to include:
company logo and name (Pelton|Marsh & Quillan)
on the back, we would definitely include:
address, email, cell #
logo and name (smaller size than front)

The variable will be location of individual name and title (mine for example is ) - whether on the front OR on the back. interested in variations from which to choose
Dr. Neil R. Whitcombe, CFA
Scientifique des Fusées Financières

we would like to use contemporary symbols for address, email address, cell # with an option for web site that we do not intend to use initially. we like two sided cards and believe this design should use four rounded corners with the standard size. we prefer thicker card stock and may look at metal.

```html
<!DOCTYPE html>
<html lang="fr">
<head>
<meta charset="utf-8">
<title>Pelton|Marsh &amp; Quillan — Business Card</title>
<link rel="stylesheet" href="https://fonts.googleapis.com/css2?family=Lato:wght@400;700&display=swap">
<style>
  :root {
    --backdrop: #1d1d1d;
    --card: #131313;
    --silver: #a9a9a9;
    --grey-text: #8c8c8c;
    --orange: #e07a1f;
    --shadow: rgba(0, 0, 0, 0.55);
  }
  * { box-sizing: border-box; margin: 0; padding: 0; }
  html, body {
    width: 1200px;
    height: 900px;
    overflow: hidden;
    background: var(--backdrop);
    font-family: "Lato", Arial, sans-serif;
  }
  .stage { position: relative; width: 1200px; height: 900px; }
  .card {
    position: absolute;
    width: 560px;
    height: 320px;
    background: var(--card);
    border-radius: 14px;
    box-shadow: 0 18px 40px var(--shadow);
  }
  .card--front { left: 60px; top: 80px; }
  .card--back  { left: 580px; top: 490px; }

  .wordmark {
    display: flex;
    align-items: center;
    gap: 12px;
    white-space: nowrap;
    font-weight: 400;
  }
  .wordmark__square { display: block; }

  .card--front .wordmark {
    position: absolute;
    left: 0; right: 0; top: 0; bottom: 0;
    justify-content: center;
    font-size: 34px;
    letter-spacing: 1px;
    color: var(--silver);
  }
  .card--front .wordmark__square { width: 22px; height: 22px; background: var(--silver); }

  .card--back .wordmark {
    position: absolute;
    right: 36px;
    top: 58px;
    font-size: 20px;
    letter-spacing: 0.5px;
    color: var(--grey-text);
  }
  .card--back .wordmark__square { width: 14px; height: 14px; background: var(--orange); }

  .rule {
    position: absolute;
    left: 330px;
    right: 30px;
    top: 150px;
    height: 1px;
    background: var(--orange);
  }
  .person { position: absolute; left: 36px; top: 132px; }
  .person__name {
    font-size: 21px;
    font-weight: 700;
    color: var(--orange);
    letter-spacing: 0.2px;
  }
  .person__title {
    margin-top: 4px;
    font-size: 14px;
    color: var(--grey-text);
  }
  .contacts {
    position: absolute;
    left: 44px;
    top: 208px;
    list-style: none;
  }
  .contacts__item {
    display: flex;
    align-items: center;
    gap: 10px;
    font-size: 14px;
    color: var(--grey-text);
    line-height: 26px;
  }
  .contacts__icon { width: 13px; height: 13px; fill: var(--orange); flex: none; }
  .address {
    position: absolute;
    right: 36px;
    top: 212px;
    text-align: right;
    font-size: 14px;
    line-height: 20px;
    color: var(--grey-text);
    font-style: normal;
  }
</style>
</head>
<body>
<main class="stage">

  <section class="card card--front" aria-label="Card front">
    <div class="wordmark">
      <span class="wordmark__square" aria-hidden="true"></span>
      <span class="wordmark__name">Pelton|Marsh &amp; Quillan</span>
    </div>
  </section>

  <section class="card card--back" aria-label="Card back">
    <div class="wordmark">
      <span class="wordmark__square" aria-hidden="true"></span>
      <span class="wordmark__name">Pelton|Marsh &amp; Quillan</span>
    </div>

    <div class="rule" aria-hidden="true"></div>

    <div class="person">
      <p class="person__name">Dr. Neil R. Whitcombe, CFA</p>
      <p class="person__title">Scientifique des Fusées Financières</p>
    </div>

    <ul class="contacts">
      <li class="contacts__item">
        <svg class="contacts__icon" viewBox="0 0 16 16" aria-hidden="true">
          <path d="M3.2 1.2l2.4 0 1.2 3.2-1.6 1.2c.8 1.8 2.4 3.4 4.2 4.2l1.2-1.6 3.2 1.2v2.4c0 .9-.8 1.6-1.7 1.6C6.6 13.4 2.6 9.4 1.6 2.9 1.6 2 2.3 1.2 3.2 1.2z"/>
        </svg>
        <span>555-014-2290</span>
      </li>
      <li class="contacts__item">
        <svg class="contacts__icon" viewBox="0 0 16 16" aria-hidden="true">
          <path d="M1 3h14v10H1z M1.8 3.8l6.2 4.8 6.2-4.8" fill="none" stroke="#e07a1f" stroke-width="1.6"/>
        </svg>
        <span>info@pmquillan.com</span>
      </li>
      <li class="contacts__item">
        <svg class="contacts__icon" viewBox="0 0 16 16" aria-hidden="true">
          <circle cx="8" cy="8" r="6.5" fill="none" stroke="#e07a1f" stroke-width="1.6"/>
          <path d="M1.5 8h13M8 1.5c-2.4 2.4-2.4 10.6 0 13M8 1.5c2.4 2.4 2.4 10.6 0 13" fill="none" stroke="#e07a1f" stroke-width="1.2"/>
        </svg>
        <span>www.pmquillan.com</span>
      </li>
    </ul>

    <address class="address">
      410 Alder Lane 9th Floor<br>
      Hartwell, NY 10990
    </address>
  </section>

</main>
</body>
</html>
```